Velora Pedalworks

We are a new start up company selling (online) innovative cycling products.
Being a new player in the market a modern eye catching logo would be good.
Initially selling safety tail lights with blinkers & modern designed cycling gloves and eventually extending our range into cycling clothing. Many of our products will have a safety theme.

Please see logo attached.

Reason: I have extended deadline because i have just received the Logo to be used.

Target Market(s)

We will be target marketing to the young 20-30year old trendy commuter cyclists to the 40 - 60 year old weekend road riders with there immaculate color coordinated road bikes & clothing.

Industry/Entity Type

Safety

Requirements
Must have
• Name: Mavin Tolby
Line for Mobile No. 0438 261 905
Line for email Address: mavin@velorapedalworks.example.com.au
3 Lines for Postal Address: PO Box 3862
Wattle Crest Corner
NSW 2174
Website: www.velorapedalworks.example.com.au

```html
<!DOCTYPE html>
<html lang="en">
<head>
<meta charset="utf-8">
<title>Velora Pedalworks — Business Card</title>
<link rel="stylesheet" href="https://fonts.googleapis.com/css2?family=Open+Sans:wght@400;600;700&display=swap">
<style>
  :root {
    --backdrop: #e9e6e1;
    --card-white: #ffffff;
    --card-shade: #efefef;
    --ink: #2b2b2b;
    --ink-soft: #555555;
    --charcoal: #262626;
    --charcoal-light: #3a3a3a;
    --amber: #f0a81c;
    --amber-deep: #e08e12;
    --on-dark: #f4f4f4;
  }
  * { box-sizing: border-box; margin: 0; padding: 0; }
  html, body {
    width: 1200px; height: 1023px; overflow: hidden;
    background: var(--backdrop);
    font-family: "Open Sans", Arial, sans-serif;
  }
  .business-card {
    position: absolute; left: 150px; top: 254px;
    width: 900px; height: 514px;
    background: linear-gradient(135deg, var(--card-white) 40%, var(--card-shade));
    box-shadow: 0 18px 40px rgba(0,0,0,.25);
    overflow: hidden;
  }
  .address-band {
    position: absolute; left: 0; bottom: 0; width: 100%; height: 160px;
    background: linear-gradient(180deg, var(--charcoal-light), var(--charcoal));
  }
  .name-panel {
    position: absolute; left: 0; top: 0; width: 900px; height: 514px;
  }
  .brand {
    position: absolute; left: 56px; top: 104px;
    display: flex; align-items: center; gap: 16px;
  }
  .brand-dot {
    width: 34px; height: 34px; border-radius: 50%; background: var(--amber);
  }
  .brand-name {
    font-size: 56px; font-weight: 600; color: var(--ink); letter-spacing: -1px;
  }
  .brand-web {
    position: absolute; left: 58px; top: 186px;
    font-size: 19px; letter-spacing: 3px; color: var(--ink-soft);
  }
  .person {
    position: absolute; left: 50px; top: 318px; color: #fff;
  }
  .person-name { font-size: 38px; font-weight: 700; letter-spacing: 1px; line-height: 1.1; }
  .person-role { font-size: 22px; margin-bottom: 12px; }
  .contact-line {
    display: flex; align-items: center; gap: 10px;
    font-size: 18px; line-height: 1.55;
  }
  .contact-icon { width: 16px; height: 16px; flex: none; }
  .postal {
    position: absolute; left: 560px; top: 386px; color: var(--on-dark);
    font-size: 22px; line-height: 1.4; letter-spacing: 1px;
  }
  .postal-first { display: flex; align-items: center; gap: 10px; }
</style>
</head>
<body>
  <section class="business-card">
    <div class="address-band"></div>

    <svg class="name-panel" viewBox="0 0 900 514" aria-hidden="true">
      <defs>
        <linearGradient id="amberFill" x1="0" y1="0" x2="1" y2="1">
          <stop offset="0" stop-color="var(--amber)"/>
          <stop offset="1" stop-color="var(--amber-deep)"/>
        </linearGradient>
      </defs>
      <polygon points="0,296 440,296 500,514 0,514" fill="url(#amberFill)"/>
    </svg>

    <div class="brand">
      <span class="brand-dot"></span>
      <span class="brand-name">Velora Pedalworks</span>
    </div>
    <div class="brand-web">www.velorapedalworks.example.com.au</div>

    <div class="person">
      <div class="person-name">MAVIN TOLBY</div>
      <div class="person-role">Director</div>
      <div class="contact-line">
        <svg class="contact-icon" viewBox="0 0 16 16" aria-label="Mobile"><rect x="3" y="0.5" width="10" height="15" rx="2" fill="#fff"/><rect x="5" y="2.5" width="6" height="9" fill="var(--amber)"/></svg>
        <span>0438 261 905</span>
      </div>
      <div class="contact-line">
        <svg class="contact-icon" viewBox="0 0 16 16" aria-label="Email"><rect x="0.5" y="3" width="15" height="10" rx="1" fill="#fff"/><polyline points="1,4 8,9 15,4" fill="none" stroke="var(--amber)" stroke-width="1.5"/></svg>
        <span>mavin@velorapedalworks.example.com.au</span>
      </div>
    </div>

    <div class="postal">
      <div class="postal-first">
        <svg class="contact-icon" viewBox="0 0 16 16" aria-label="Postal address"><rect x="1" y="3" width="14" height="10" rx="1" fill="var(--on-dark)"/><polyline points="1.5,4 8,9 14.5,4" fill="none" stroke="var(--charcoal)" stroke-width="1.5"/></svg>
        <span>PO Box 3862</span>
      </div>
      <div>Wattle Crest Corner</div>
      <div>NSW 2174</div>
    </div>
  </section>
</body>
</html>
```